依頼詳細
弊社がお客様にお渡ししているパンフレットに添えたいと思っております。白樺工房が使用している断熱材をわかりやすくお客様に伝えるためのチラシを作成したいと考えているため、炭化コルクの性能をわかりやすく伝わるように写真・イラストを使用しながら、お客様が興味を持っていただくようなチラシの作成をお願い致します。

◎加えていただきたい内容
タイトル:炭に包まれた内断熱のお家

1.炭化コルクの優れた5つの性能
①断熱性能(スペースシャトルの断熱材としても使用されていました。)
②防虫性能(スぺリンという物質が虫やダニを寄せ付けません。)
③防音性能(優れた防音性能と吸音性、衝撃吸収性により音の振動を遮ります。)
④調湿性能(空気中の余分な水分を吸収、乾燥時ははき出したりすることで、室内の結露やカビの発生を防ぎます。)
⑤消臭性能(多孔質な炭の効果で、ペット臭などの嫌なにおいを吸着消臭します。)
※わかりやすくなるようイラスト添えでお願い致します。

2.炭化コルク+漆喰でつくる「空気のおいしい家」
ベルタスホームの健康住宅
漆喰と炭の効果で24時間サラッとした空気か365日続きます。

ジメジメした雨の日も室内はカラッと調湿する100%
天然素材の断熱材「炭化コルク」
天井と壁に炭化コルクが入っていて、内断熱になっているため
夏涼しく、冬暖かい室内にしてくれます。
(一般的な住宅メーカーは、クレナライトと呼ばれる発泡スチロールのような断熱材を天井部分にしか使用していないのですが、ベルタスホームは、炭化コルクの断熱材を天井と日の当たる壁一面に貼っております。イラスト参考になるかと思いますので、実際の比較施工写真を添付いたします。

3.炭化コルクとは?
コルクの木の樹皮からできています。
高温で蒸し焼きにするとコルク自身のヤニで固形化するため、シックハウスの原因となる価格接着剤を使用しない、天然コルク100%の断熱材です。

4.使用していただきたいお家の画像
実際に施工したお家の内装の写真を使用していただきたい画像を添付いたしますので、ご確認宜しくお願い致します。

★重要★
炭化コルクの良さである内断熱と調湿効果が分かりやすいものになるようイラストを用いて作っていただけますようお願い申し上げます。

データをイラレとJPGで頂けますと幸いです。
何卒よろしくお願い申し上げます。
記載項目
ベルタスホーム/チラシ
サイズ
A4
ページ数
片面
希望イメージ
シンプル 複雑
単色 カラフル
暗い 明るい
日常 高級
遊び心 厳粛
未来的 伝統的
女性的 男性的
希望する色
黄・オレンジ系、茶系
納品ファイル
• 高解像度JPG (.jpg)
• イラストレーター形式 (.ai)
補足説明
縦のA4サイズで作成お願い致します。
ファイルに添付してあります写真と、サンプルを利用して作成してくださいますようお願い申し上げます。
■ 選んだ理由

弊社のイメージカラーであるオレンジをすっきりとまとめて配置されていた点、弊社の使用している断熱材をわかりやすい且つ、伝わりやすくデザインしていただいた点や、何度も修正依頼をさせていただいたのにも関わらず真摯に対応していただいた点に惹かれ選ばせていただきました。イラストも見た目が可愛らしく伝わる内容であった点が気に入りました。ありがとうございました。

■ 提案者全員のお礼・コメント

この度は、ベルタスホーム株式会社の断熱材チラシにご応募いただき、誠にありがとうございました。年末の忙しい時期にも関わらず皆様のアイディアをいただけたこと誠に感謝しております。多くの素晴らしいアイディアをいただいた中から選ぶことは、とても難しい作業でした。どれもベルタスホームの雰囲気にあったものばかりでこんなにも多くの良い作品に出合えたことを大変うれしく思います。また、ご依頼をさせて頂く際もご一緒にお仕事させて頂きたいと思いますので、何卒よろしくお願い申し上げます。誠にありがとうございました。

```html
<!DOCTYPE html>
<html lang="ja">
<head>
<meta charset="utf-8">
<title>炭に包まれた内断熱のお家 | ベルタスホーム</title>
<link rel="stylesheet" href="https://fonts.googleapis.com/css2?family=Noto+Sans+JP:wght@400;700;900&family=Noto+Serif+JP:wght@700;900&display=swap">
<style>
:root{
  --yellow:#f5c518;
  --red:#c8161d;
  --ink:#1a1a1a;
  --brown:#5a3a20;
  --white:#ffffff;
  --grey:#8a8a8a;
}
*{margin:0;padding:0;box-sizing:border-box}
html,body{width:846px;height:1200px;overflow:hidden;background:var(--white)}
body{font-family:"Noto Sans JP",sans-serif;color:var(--ink)}
.flyer{position:relative;width:846px;height:1200px;overflow:hidden;background:var(--white)}
.flyer > *{position:absolute}

.hero-photo{left:0;top:0;width:846px;height:430px;z-index:0;
  background:linear-gradient(180deg,#f4f2ee 0%,#e4ded5 40%,#3a3532 72%,#2a2624 100%)}
.headline{left:22px;top:16px;z-index:2}
.headline .kicker{display:inline-block;background:var(--white);color:var(--red);font-weight:700;font-size:22px;padding:2px 10px;letter-spacing:2px}
.headline .main{display:block;margin-top:6px;background:var(--ink);color:var(--white);font-family:"Noto Serif JP",serif;font-weight:900;font-size:38px;padding:4px 14px;letter-spacing:1px}
.headline .main em{font-style:normal;color:var(--yellow)}

.yellow-field{left:0;top:430px;width:846px;height:715px;background:var(--yellow);z-index:0}
.house-illust{left:170px;top:382px;width:506px;height:168px;z-index:1;
  background:linear-gradient(180deg,#fbfbfb,#dcd6cc);border-radius:6px}

.features{left:22px;top:206px;width:802px;display:flex;justify-content:space-between;z-index:3}
.feature{width:150px;text-align:center}
.feature .badge{width:120px;height:120px;margin:0 auto;border-radius:50%;background:var(--yellow);border:4px solid var(--white);
  display:flex;align-items:center;justify-content:center;font-family:"Noto Serif JP",serif;font-weight:900;font-size:36px;color:var(--red)}
.feature .note{margin-top:6px;font-size:12px;color:var(--white);line-height:1.35;font-weight:700}

.title-block{left:30px;top:556px;z-index:2}
.title-block .ruby{font-size:20px;font-weight:700;margin-left:14px;display:block;line-height:1.2}
.title-block h1{font-family:"Noto Serif JP",serif;font-weight:900;font-size:52px;line-height:1.15}
.title-block h1 .accent{color:var(--red);font-size:68px}

.cork-box{left:530px;top:580px;width:290px;z-index:2}
.cork-box .label{border:3px solid var(--ink);background:var(--white);text-align:center;padding:6px 0 8px}
.cork-box .label span{display:block;font-family:"Noto Serif JP",serif;font-weight:900;font-size:30px;line-height:1.25}
.cork-box .label span + span{background:var(--ink);color:var(--white);margin:4px 10px 0}
.cork-box p{margin-top:10px;font-size:12.5px;line-height:1.55}

.site-photos{left:30px;top:740px;width:210px;z-index:2}
.site-photos .shot{height:118px;background:linear-gradient(135deg,#6d5a46,#a08c74);border:3px solid var(--white)}
.site-photos .caption{font-size:12px;font-weight:700;margin:6px 0 10px}

.moisture{left:258px;top:740px;width:240px;z-index:2}
.moisture .lead{font-size:16px;font-weight:700;line-height:1.45}
.moisture .lead strong{color:var(--red)}
.moisture p{margin-top:8px;font-size:12.5px;line-height:1.55}
.moisture .chair-illust{margin-top:10px;height:110px;background:linear-gradient(180deg,#fff3c4,#f2d77a);border-radius:55px 55px 8px 8px}

.cork-photos{left:530px;top:800px;width:290px;display:flex;gap:8px;z-index:2}
.cork-photos div{flex:1;height:130px;border:3px solid var(--white)}
.cork-photos .charred{background:linear-gradient(135deg,#2d2a27,#54504b)}
.cork-photos .plaster{background:linear-gradient(135deg,#f3efe6,#d9cdb5)}

.health{left:530px;top:950px;width:290px;text-align:center;z-index:2}
.health h2{font-size:18px;font-weight:900;color:var(--brown);border-bottom:2px solid var(--brown);padding-bottom:3px}
.health p{margin-top:6px;font-size:12.5px;line-height:1.5}

.footer{left:0;top:1145px;width:846px;height:55px;background:var(--white);display:flex;align-items:center;padding:0 24px;gap:14px;border-top:4px solid var(--red);z-index:2}
.footer .mark{width:14px;height:14px;background:var(--red)}
.footer .company{font-size:19px;font-weight:900}
.footer .address{font-size:11px;color:var(--grey)}
.footer .tel{margin-left:auto;font-size:20px;font-weight:900}
.footer .tel small{font-size:12px;font-weight:700;margin-right:4px}
</style>
</head>
<body>
<main class="flyer">
  <div class="hero-photo" role="img" aria-label="白い壁と吹き抜けのある明るいリビングの内装写真"></div>
  <div class="yellow-field"></div>
  <div class="house-illust" role="img" aria-label="天井と壁に炭化コルクが入った家の断面イラスト"></div>

  <header class="headline">
    <span class="kicker">天然素材の断熱材</span>
    <span class="main"><em>炭化コルク</em> 優れた守るチカラ!!</span>
  </header>

  <section class="features" aria-label="炭化コルクの5つの性能">
    <div class="feature"><div class="badge">断熱</div><p class="note">スペースシャトルにも<br>採用の断熱材</p></div>
    <div class="feature"><div class="badge">防虫</div><p class="note">虫やダニを<br>寄せ付けない</p></div>
    <div class="feature"><div class="badge">防音</div><p class="note">音の振動を<br>遮ります</p></div>
    <div class="feature"><div class="badge">調湿</div><p class="note">結露・カビの発生を<br>防ぎます</p></div>
    <div class="feature"><div class="badge">消臭</div><p class="note">ペット臭などを<br>吸着消臭</p></div>
  </section>

  <div class="title-block">
    <span class="ruby">すみ</span>
    <h1><span class="accent">炭</span>に包まれた<br>内断熱のお家</h1>
  </div>

  <div class="cork-box">
    <div class="label"><span>天井と壁に</span><span>炭化コルク</span></div>
    <p>コルクの木の樹皮からできています。高温で蒸し焼きにするとコルク自身のヤニで固形化するため、シックハウスの原因となる化学接着剤を使用しない、天然コルク100%の断熱材です。</p>
  </div>

  <div class="site-photos">
    <div class="shot" role="img" aria-label="一般的な住宅の天井断熱の施工写真"></div>
    <p class="caption">一般的な住宅：天井のみ</p>
    <div class="shot" role="img" aria-label="ベルタスホームの天井と壁の炭化コルク施工写真"></div>
    <p class="caption">ベルタスホーム：天井と壁</p>
  </div>

  <div class="moisture">
    <p class="lead">ジメジメした雨の日も<br>室内はカラッと調湿！<br><strong>100%天然素材の<br>断熱材「炭化コルク」</strong></p>
    <p>夏涼しく、冬暖かい。一般的なクレナライトと違い、天井と日の当たる壁一面に貼っています。</p>
    <div class="chair-illust" role="img" aria-label="快適な室内でくつろぐ椅子のイラスト"></div>
  </div>

  <div class="cork-photos">
    <div class="charred" role="img" aria-label="炭化コルクの断熱材の写真"></div>
    <div class="plaster" role="img" aria-label="漆喰の壁の写真"></div>
  </div>

  <div class="health">
    <h2>ベルタスホームの健康住宅</h2>
    <p>炭化コルク＋漆喰でつくる「空気のおいしい家」。24時間サラッとした空気が365日続きます。</p>
  </div>

  <footer class="footer">
    <span class="mark"></span>
    <span class="company">ベルタスホーム株式会社</span>
    <span class="address">大分県森野市緑ヶ丘3-8-12</span>
    <span class="tel"><small>フリーダイヤル</small>0120-555-214</span>
  </footer>
</main>
</body>
</html>
```